Transparent Real Estate Experience

Looking for an Image/Graphic for a postcard and brochure that communicates a complete transparent experience when selling a home.
The image is to convey "seeing through", hence transparent or transparency. NO Hourglasses or magnifying glasses. To me, those convey different messages - hour glass is "time" and magnifying is "making something small look bigger".

Ideally, a glass house with the words under the glass so the house is transparent to the words that are being communicated.

Those are:
transparency, honesty, communication, integrity, ethics, clarity, principles, knowledge, experience, trust, fairness, responsibility.

OR - using a "glass font" with those words in a mosaic order so the words are all transparent.

Professional Look - no cartoons...See samples - only thing I could find to provide a starting point. Thanks!
Updates

Target Market(s)

People selling their homes

Industry/Entity Type

Real Estate

Colors
0054AA
0677BA
7BADD7
CADEEF
E8F1F8

Requirements
Must have
• "Transparent" Look - "See-through"
Should not have
• Cartoons

```html
<!DOCTYPE html>
<html lang="en">
<head>
<meta charset="UTF-8">
<title>Transparent Real Estate Experience</title>
<link href="https://fonts.googleapis.com/css2?family=Playfair+Display:ital,wght@1,900&display=swap" rel="stylesheet">
<style>
  :root {
    --bg-center: #f6f4ee;
    --bg-edge: #dcd9d0;
    --ghost: #d6d2c8;
    --glass-light: #ffffff;
    --glass-mid: #c9c9c7;
    --glass-dark: #8f8f8c;
    --glass-edge: #7c7c78;
    --house-wood: #8a5a3a;
    --house-slate: #4a4a4a;
    --house-glass: #cfd6d4;
  }
  html, body {
    margin: 0;
    padding: 0;
    overflow: hidden;
  }
  body {
    width: 1200px;
    height: 900px;
  }
  .values-canvas {
    position: relative;
    width: 1200px;
    height: 900px;
    background: radial-gradient(ellipse at 50% 48%, var(--bg-center) 0%, #eeebe4 45%, var(--bg-edge) 100%);
    overflow: hidden;
  }
  .values-art {
    position: absolute;
    inset: 0;
    width: 1200px;
    height: 900px;
  }
  .word {
    font-family: "Playfair Display", Georgia, serif;
    font-style: italic;
    font-weight: 900;
  }
  .word--ghost {
    fill: var(--ghost);
    opacity: 0.75;
  }
  .word--glass {
    fill: url(#glassFill);
    stroke: var(--glass-edge);
    stroke-width: 1.1;
    paint-order: stroke fill;
    filter: url(#glassShadow);
  }
</style>
</head>
<body>
<main class="values-canvas">
  <svg class="values-art" viewBox="0 0 1200 900" xmlns="http://www.w3.org/2000/svg">
    <defs>
      <linearGradient id="glassFill" x1="0" y1="0" x2="0" y2="1">
        <stop offset="0" stop-color="var(--glass-light)"/>
        <stop offset="0.35" stop-color="#f1f1ef"/>
        <stop offset="0.55" stop-color="var(--glass-mid)"/>
        <stop offset="0.8" stop-color="#f7f7f5"/>
        <stop offset="1" stop-color="var(--glass-dark)"/>
      </linearGradient>
      <linearGradient id="houseTone" x1="0" y1="0" x2="1" y2="1">
        <stop offset="0" stop-color="var(--house-slate)"/>
        <stop offset="0.45" stop-color="var(--house-wood)"/>
        <stop offset="0.7" stop-color="var(--house-glass)"/>
        <stop offset="1" stop-color="#5c5c58"/>
      </linearGradient>
      <filter id="glassShadow" x="-10%" y="-30%" width="120%" height="160%">
        <feDropShadow dx="2" dy="3" stdDeviation="2.5" flood-color="#6b6862" flood-opacity="0.45"/>
      </filter>
      <filter id="softEdge" x="-5%" y="-5%" width="110%" height="110%">
        <feGaussianBlur stdDeviation="6"/>
      </filter>
    </defs>

    <g class="ghost-words">
      <text class="word word--ghost" x="537" y="68" font-size="46" textLength="115" lengthAdjust="spacingAndGlyphs">trust</text>
      <text class="word word--ghost" x="97" y="116" font-size="72" textLength="276" lengthAdjust="spacingAndGlyphs">integrity</text>
      <text class="word word--ghost" x="795" y="113" font-size="70" textLength="338" lengthAdjust="spacingAndGlyphs">knowledge</text>
      <text class="word word--ghost" x="240" y="240" font-size="120" textLength="743" lengthAdjust="spacingAndGlyphs">transparency</text>
      <text class="word word--ghost" x="48" y="389" font-size="56" textLength="210" lengthAdjust="spacingAndGlyphs">honesty</text>
      <text class="word word--ghost" x="952" y="388" font-size="56" textLength="191" lengthAdjust="spacingAndGlyphs">ethics</text>
      <text class="word word--ghost" x="0" y="540" font-size="66" textLength="240" lengthAdjust="spacingAndGlyphs">fairness</text>
      <text class="word word--ghost" x="997" y="540" font-size="60" textLength="188" lengthAdjust="spacingAndGlyphs">clarity</text>
      <text class="word word--ghost" x="225" y="730" font-size="104" textLength="720" lengthAdjust="spacingAndGlyphs">communication</text>
      <text class="word word--ghost" x="71" y="832" font-size="76" textLength="379" lengthAdjust="spacingAndGlyphs">experience</text>
      <text class="word word--ghost" x="667" y="832" font-size="76" textLength="469" lengthAdjust="spacingAndGlyphs">responsibility</text>
    </g>

    <g class="house-visual" role="img" aria-label="Modern two-storey glass house with wood and slate cladding, trees on both sides and a landscaped terrace">
      <ellipse cx="607" cy="455" rx="300" ry="175" fill="#ffffff" opacity="0.6" filter="url(#softEdge)"/>
      <rect x="330" y="300" width="555" height="300" rx="6" fill="url(#houseTone)" opacity="0.85"/>
    </g>

    <g class="glass-words">
      <text class="word word--glass" x="544" y="141" font-size="44" textLength="97" lengthAdjust="spacingAndGlyphs">trust</text>
      <text class="word word--glass" x="180" y="178" font-size="62" textLength="229" lengthAdjust="spacingAndGlyphs">integrity</text>
      <text class="word word--glass" x="757" y="174" font-size="62" textLength="282" lengthAdjust="spacingAndGlyphs">knowledge</text>
      <text class="word word--glass" x="300" y="281" font-size="100" textLength="611" lengthAdjust="spacingAndGlyphs">transparency</text>
      <text class="word word--glass" x="142" y="401" font-size="48" textLength="180" lengthAdjust="spacingAndGlyphs">honesty</text>
      <text class="word word--glass" x="911" y="404" font-size="48" textLength="131" lengthAdjust="spacingAndGlyphs">ethics</text>
      <text class="word word--glass" x="97" y="534" font-size="58" textLength="218" lengthAdjust="spacingAndGlyphs">fairness</text>
      <text class="word word--glass" x="922" y="533" font-size="52" textLength="158" lengthAdjust="spacingAndGlyphs">clarity</text>
      <text class="word word--glass" x="289" y="684" font-size="96" textLength="592" lengthAdjust="spacingAndGlyphs">communication</text>
      <text class="word word--glass" x="161" y="776" font-size="66" textLength="311" lengthAdjust="spacingAndGlyphs">experience</text>
      <text class="word word--glass" x="649" y="776" font-size="66" textLength="390" lengthAdjust="spacingAndGlyphs">responsibility</text>
    </g>
  </svg>
</main>
</body>
</html>
```